Harwick Legal

To update and modernize current business card appearance. Marta's business is based in Melbourne with 4 other lawyers in the firm. Marta travels to the Pilbara in Western Australia approximately 1 week a month as part of the firms legal work. She consults with clients in Newman, Tom Price and Port Hedland. The lawyers work mostly from a home office, apart from court appearances. They have a virtual office in Melbourne city, and use facilities in 3 or 4 other locations around Melbourne. It is important the client's think this is a conventional law firm with a permanent office. Our business structure is a difficult concept for them to grasp. The business has been operational for 3 years, growing from 1 lawyer to 4 lawyers during that time. Our website is www.Harwicklegal.example.au and is currently being upgraded as we are not happy with its content. The logo is currently orange and dark grey but the orange is a difficult colour to reproduce and often turns out "poo" brown when documents are printed. We need clients to know we are user friendly and caring - and not head up our rears ends as some lawyers appear to be.
Updates

Thank you for the feedback so far. 1. Some of the designs have too much black (We prefer darker grey & not too much.) 2. Happy for designers to play around with different colours & logo design. What we're after is a modern look and business card that people say "wow" when they pick it up.

Industry/Entity Type

Business

```html
<!DOCTYPE html>
<html lang="en">
<head>
<meta charset="utf-8">
<title>Harwick Legal – Business Cards</title>
<link rel="stylesheet" href="https://fonts.googleapis.com/css2?family=Cinzel:wght@400;700&family=Cormorant+Garamond:wght@500;700&display=swap">
<style>
  :root {
    --backdrop: #3b3b3b;
    --maroon: #5a1614;
    --maroon-deep: #3f0f0d;
    --cream: #f3e0c6;
    --cream-light: #f8ecdb;
    --tan: #c48a66;
    --rust: #8e3418;
    --rust-deep: #611b0e;
    --ivory: #f6ead8;
  }
  * { box-sizing: border-box; margin: 0; padding: 0; }
  html, body { width: 1200px; height: 800px; overflow: hidden; }
  body {
    background: var(--backdrop);
    display: flex;
    align-items: center;
    justify-content: center;
    gap: 40px;
    font-family: "Cinzel", "Times New Roman", serif;
  }
  .card {
    width: 520px;
    height: 300px;
    position: relative;
    overflow: hidden;
    box-shadow: 0 10px 24px rgba(0,0,0,.45);
  }

  /* ---------- Contact side ---------- */
  .card--contact {
    background: radial-gradient(ellipse at 60% 45%, var(--cream-light), var(--cream) 70%, #e7c9a6);
    color: var(--maroon);
  }
  .edge-band {
    position: absolute;
    top: 0; bottom: 0;
    width: 38px;
    background: linear-gradient(180deg, #e9c6a6, #c98e6a 30%, #f4e2cc 55%, #b9785a 80%, #e9c6a6);
    opacity: .75;
  }
  .edge-band--left { left: 0; }
  .edge-band--right { right: 0; }
  .rule {
    position: absolute;
    left: 60px; right: 60px;
    height: 2px;
    background: linear-gradient(90deg, transparent, var(--maroon) 20%, var(--maroon) 80%, transparent);
  }
  .rule--top { top: 34px; }
  .rule--bottom { bottom: 34px; }
  .brand {
    position: absolute;
    left: 50px;
    top: 92px;
    width: 160px;
    text-align: center;
  }
  .brand__mark {
    display: block;
    width: 62px; height: 62px;
    margin: 0 auto 10px;
    border-radius: 50%;
    background: var(--maroon);
  }
  .brand__name {
    font-size: 23px;
    font-weight: 400;
    letter-spacing: 2px;
    line-height: 1.1;
    color: var(--tan);
  }
  .details {
    position: absolute;
    left: 216px;
    right: 46px;
    top: 52px;
    text-align: center;
    white-space: nowrap;
  }
  .ribbon {
    display: inline-block;
    background: var(--maroon);
    color: var(--ivory);
    font-size: 16px;
    font-weight: 700;
    letter-spacing: 1px;
    padding: 4px 16px;
    position: relative;
  }
  .ribbon::before, .ribbon::after {
    content: "";
    position: absolute;
    top: 5px;
    border: 12px solid var(--maroon-deep);
  }
  .ribbon::before { left: -16px; border-left-color: transparent; z-index: -1; }
  .ribbon::after { right: -16px; border-right-color: transparent; z-index: -1; }
  .credentials {
    font-family: "Cormorant Garamond", Georgia, serif;
    font-size: 9px;
    letter-spacing: .5px;
    line-height: 1.2;
    margin-top: 5px;
    text-transform: uppercase;
  }
  .phone-main {
    font-size: 15px;
    font-weight: 700;
    margin-top: 7px;
  }
  .contact-line {
    font-size: 9px;
    letter-spacing: 0;
    line-height: 1.6;
  }
  .phone-main + .contact-line { margin-top: 3px; }
  .region {
    font-size: 10px;
    font-weight: 700;
    line-height: 1.4;
    margin-top: 5px;
  }

  /* ---------- Practice side ---------- */
  .card--practice {
    background: radial-gradient(ellipse at 50% 40%, var(--rust), var(--rust-deep) 85%);
    color: var(--ivory);
    text-align: center;
  }
  .texture {
    position: absolute;
    inset: 0;
    background: linear-gradient(135deg, rgba(255,170,110,.12), rgba(0,0,0,.12) 50%, rgba(255,170,110,.1));
  }
  .card--practice .brand {
    left: 0; right: 0; top: 42px; width: auto;
  }
  .card--practice .brand__mark {
    background: var(--ivory);
    width: 70px; height: 70px;
  }
  .card--practice .brand__name {
    color: var(--ivory);
    font-size: 26px;
  }
  .practice {
    position: absolute;
    left: 20px; right: 20px;
    top: 200px;
    font-size: 11px;
    letter-spacing: .5px;
    line-height: 1.6;
  }
  .practice__title { font-weight: 700; letter-spacing: 1.5px; }
</style>
</head>
<body>

  <section class="card card--practice" aria-label="Card back">
    <div class="texture" role="img" aria-label="Subtle diamond lattice texture"></div>
    <div class="brand">
      <span class="brand__mark"></span>
      <p class="brand__name">Harwick<br>Legal</p>
    </div>
    <div class="practice">
      <p class="practice__title">AREAS OF PRACTICE:</p>
      <p>Family Law | Collaborative Practice | Mediation &amp; Negotiation</p>
      <p>Intervention Orders | Criminal Law</p>
    </div>
  </section>

  <section class="card card--contact" aria-label="Card front">
    <div class="edge-band edge-band--left" role="img" aria-label="Diamond pattern border"></div>
    <div class="edge-band edge-band--right" role="img" aria-label="Diamond pattern border"></div>
    <div class="rule rule--top"></div>
    <div class="rule rule--bottom"></div>

    <div class="brand">
      <span class="brand__mark"></span>
      <p class="brand__name">Harwick<br>Legal</p>
    </div>

    <div class="details">
      <p class="ribbon">J. MARTA PENROSE</p>
      <p class="credentials">LLB(Hons) – Accredited Mediator<br>Principal Solicitor</p>
      <p class="phone-main">1300 HARWICK (427 942)</p>
      <p class="contact-line">M: 0400 555 018</p>
      <p class="contact-line">MARTA.PENROSE@HARWICKLEGAL.EXAMPLE.AU</p>
      <p class="contact-line">WWW.HARWICKLEGAL.EXAMPLE.AU</p>
      <p class="region">MELBOURNE<br>EASTERN AND BAYSIDE SUBURBS</p>
    </div>
  </section>

</body>
</html>
```